I had to make an update to properly guide your designs.
I need a brochure for a company called Brevant Oakmere Ltd. all details you need can be found in the attached files including content in a microsoft word file. in the word file you will see the content you need please use them. you can. It is a consulting, construction and real estate company. You are free to add other relevant picture of yours that can make more sense. i have also attached the pictures needed. the word file show the usage of the pictures and the required content for them. It is pertinent to keep the design professional.
please be creative without the design appearing too crowded.
Updates
I had to make an update to properly guide your designs. i have attached a microsoft word file and pictures

```html
<!DOCTYPE html>
<html lang="en">
<head>
<meta charset="utf-8">
<title>Brevant Oakmere Ltd. – Brochure</title>
<link href="https://fonts.googleapis.com/css2?family=Source+Sans+3:wght@400;600&display=swap" rel="stylesheet">
<style>
  :root {
    --brand-red: #d81e2c;
    --brand-blue: #2b98dc;
    --sky-light: #67b3e8;
    --sky-deep: #1a8dd8;
    --ink: #1d1d1d;
    --paper: #ffffff;
    --photo-warm: #c39a5a;
    --photo-dark: #5a4a2c;
  }
  * { box-sizing: border-box; margin: 0; padding: 0; }
  html, body { width: 1200px; height: 922px; overflow: hidden; background: var(--paper); }
  body { font-family: "Source Sans 3", sans-serif; color: var(--ink); }

  .brochure { position: relative; width: 1200px; height: 922px; overflow: hidden; }

  /* Left panel */
  .info-panel { position: absolute; left: 0; top: 0; width: 407px; height: 922px; background: var(--paper); }
  .wordmark {
    position: absolute; color: var(--brand-red); font-weight: 600;
    letter-spacing: 0.5px; line-height: 1;
  }
  .wordmark--panel { left: 150px; top: 38px; font-size: 26px; }
  .wordmark--cover { left: 872px; top: 284px; font-size: 31px; }
  .wordmark span { display: block; }
  .wordmark span + span { margin-left: 22px; margin-top: 4px; }

  .section-tab {
    position: absolute; height: 46px; background: var(--brand-blue); color: var(--paper);
    font-size: 22px; line-height: 46px; border-radius: 0 24px 24px 0;
    box-shadow: 2px 4px 5px rgba(0,0,0,0.3);
  }
  .section-tab--company { left: 12px; top: 117px; width: 250px; padding-left: 28px; }
  .section-tab--aim { left: 12px; top: 574px; width: 250px; padding-left: 25px; }

  .body-copy {
    position: absolute; left: 28px; width: 372px;
    font-size: 16px; line-height: 21.5px;
  }
  .body-copy p + p { margin-top: 21.5px; }
  .body-copy--company { top: 184px; }
  .body-copy--aim { top: 642px; }

  /* Right area */
  .cover-art { position: absolute; left: 407px; top: 0; width: 793px; height: 922px; }

  .section-tab--contact {
    left: 443px; top: 318px; width: 321px; text-align: center;
    border-radius: 24px; padding: 0;
  }
  .contact-details {
    position: absolute; left: 443px; top: 407px; width: 321px; text-align: center;
    font-size: 16px; line-height: 21.5px;
  }
  .contact-details p + p { margin-top: 21px; }

  .cover-tagline {
    position: absolute; left: 806px; top: 760px; width: 390px; text-align: center;
    color: var(--paper); font-size: 20px; line-height: 26.5px;
  }
</style>
</head>
<body>
<main class="brochure">
  <section class="info-panel">
    <div class="wordmark wordmark--panel"><span>BREVANT</span><span>OAKMERE</span></div>

    <h2 class="section-tab section-tab--company">The Company</h2>
    <div class="body-copy body-copy--company">
      <p>Brevant Oakmere Ltd is a value based infrastructure development and real estate company. We are involved in planning, designing, construction and management of infrastructure development. We take on the biggest issues that affect us all, road, water, transportation, Energy and the need for places to live and work. We are proud of our ability to create and deliver good solutions to our clients whether in construction, engineering consulting and real estate.</p>
      <p>Our company is founded on a strong belief in our core values. We have a real commitment to innovation and the support of good ideas. The firm is built upon years of experience in the Nigerian Construction, consulting and real estate environment.</p>
    </div>

    <h2 class="section-tab section-tab--aim">Our Aim</h2>
    <div class="body-copy body-copy--aim">
      <p>Our mission is to develop a global infrastructure development company that will represent true industry standards and be a conspicuous player not only in Nigeria but Africa and the world over. Excellence in service remains the major driving force of the firm in the built environment. We have core values that provide guiding principles for everyone at Brevant Oakmere, these core values help us work effectively together and with others to provide a better place to work, a better service to our clients, and support to the communities in which we work.</p>
    </div>
  </section>

  <svg class="cover-art" viewBox="0 0 793 922" aria-hidden="false">
    <defs>
      <linearGradient id="sky" x1="0" y1="0" x2="1" y2="0">
        <stop offset="0" stop-color="var(--sky-light)"/>
        <stop offset="1" stop-color="var(--sky-deep)"/>
      </linearGradient>
      <linearGradient id="aerial" x1="0" y1="0" x2="1" y2="1">
        <stop offset="0" stop-color="#b08a55"/>
        <stop offset="0.45" stop-color="var(--photo-warm)"/>
        <stop offset="0.7" stop-color="#8a7a5c"/>
        <stop offset="1" stop-color="var(--photo-dark)"/>
      </linearGradient>
      <linearGradient id="edgeGlow" x1="0" y1="0" x2="1" y2="0">
        <stop offset="0" stop-color="#ffffff" stop-opacity="0"/>
        <stop offset="1" stop-color="#9fd2f3"/>
      </linearGradient>
    </defs>
    <rect class="sky-field" width="793" height="922" fill="url(#sky)"/>
    <path class="swoosh-band" d="M0,240 C260,234 540,252 793,348 L793,560 C560,640 260,675 0,676 Z" fill="#ffffff"/>
    <path class="swoosh-glow" d="M360,238 C560,250 700,290 793,330 L793,360 C700,310 560,262 360,244 Z" fill="url(#edgeGlow)"/>
    <path class="swoosh-red" d="M0,232 C260,220 540,236 793,328 L793,342 C540,250 260,236 0,241 Z" fill="var(--brand-red)"/>
    <rect class="site-photo" x="393" y="374" width="400" height="300" fill="url(#aerial)" role="img" aria-label="Aerial view of a planned city development with a lake, office blocks and green areas"/>
    <path class="swoosh-glow" d="M380,672 C560,640 700,600 793,552 L793,582 C700,620 560,658 380,680 Z" fill="#9fd2f3"/>
    <path class="swoosh-red" d="M0,672 C260,672 560,630 793,548 L793,566 C560,648 260,684 0,682 Z" fill="var(--brand-red)"/>
  </svg>

  <div class="wordmark wordmark--cover"><span>BREVANT</span><span>OAKMERE</span></div>

  <h2 class="section-tab section-tab--contact">Contact Us</h2>
  <address class="contact-details" style="font-style: normal;">
    <p>14, Halvern Street, off Corwin link Road.<br>Ikeja Lagos. Nigeria</p>
    <p>+234 15550142<br>+234 7005550187</p>
    <p>http://www.brevantoakmere.com<br>info@brevantoakmere.com</p>
  </address>

  <p class="cover-tagline">Our company is founded on a strong belief in our core values. We have a real commitment to innovation and the support of good ideas.</p>
</main>
</body>
</html>
```